Label Design for testosterone booster - NO Logo design !

I am selling mens enhancement testosterone booster and I need a new product label design.

I need a professional, premium, eye-catching (but not too exaggerated) impression.

Our target market for this products will be the USA. It needs to stand out from the other search results of the 1. page on Brivora:

https://www.brivora.com/s?k=testosterone+booster+for+men&ref=nb_sb_noss

Our bottles will be black colour.
You can play around with the colors as we are open for red, blue, green, light green colours or any nice idea you have in mind.
We prefer the enclosed designs – or somehow a mix with the best parts of this enclosed designs.
Testosterone Booster for MEN must be clear and big on the front of the packaging.
Also other important informations like: Stamina, maximum power, extra strong formula ….. and others key facts.
Made in USA with the flag is also a must, but this can be also on the read side with the other information and nutrition facts.
I want something "Eye-Catching" , with nice colors, not boring !!!!
Enclosed you find also some competitor products to give you some ideas.
Check out our favourite designs.
If you have any questions or suggestions, don´t be shy and please feel free to contact me! Better ask more than too few questions

```html
<!DOCTYPE html>
<html lang="en">
<head>
<meta charset="utf-8">
<title>Testosterone Booster for Men – Label</title>
<link rel="stylesheet" href="https://fonts.googleapis.com/css2?family=Oswald:wght@500;600;700&family=Open+Sans:wght@700;800&display=swap">
<style>
  :root {
    --backdrop: #e9ebe9;
    --label-black: #0b0b0c;
    --label-red: #d0161c;
    --deep-red: #7a0a0d;
    --white: #ffffff;
    --soft-white: #f1f1f1;
  }
  * { margin: 0; padding: 0; box-sizing: border-box; }
  html, body {
    width: 1200px; height: 900px; overflow: hidden;
    background: var(--backdrop);
  }
  .canvas {
    position: relative; width: 1200px; height: 900px;
    display: flex; align-items: center; justify-content: center;
  }
  .label {
    position: relative; width: 760px; height: 840px;
    background: var(--label-black);
    border-radius: 6px;
    overflow: hidden;
  }
  .title-band {
    position: absolute; left: 40px; right: 40px; top: 48px; height: 84px;
    display: flex; align-items: center; justify-content: center;
    background: var(--label-red);
  }
  .title-band .stripes {
    position: absolute; top: 0; height: 100%; width: 70px;
    background: repeating-linear-gradient(90deg, var(--label-black) 0 7px, var(--label-red) 7px 16px);
  }
  .title-band .stripes.left { left: 0; }
  .title-band .stripes.right { right: 0; }
  .product-name {
    font-family: "Oswald", sans-serif; font-weight: 700;
    font-size: 80px; line-height: 1; letter-spacing: 3px;
    color: var(--label-black);
  }
  .product-sub {
    position: absolute; left: 0; right: 0; top: 150px;
    text-align: center;
    font-family: "Oswald", sans-serif; font-weight: 600;
    font-size: 84px; line-height: 1; letter-spacing: 4px;
    color: var(--soft-white);
  }
  .hero-art {
    position: absolute; left: 110px; top: 270px; width: 540px; height: 380px;
    border-radius: 46% 46% 30% 30%;
    background: radial-gradient(ellipse at 50% 45%, #e3242a 0%, #b0141a 55%, #5a070a 100%);
  }
  .capsule-count {
    position: absolute; left: 40px; top: 662px; width: 66px; height: 64px;
    background: var(--label-red); color: var(--white);
    display: flex; flex-direction: column; align-items: center; justify-content: center;
    font-family: "Open Sans", sans-serif; font-weight: 800;
  }
  .capsule-count .num { font-size: 28px; line-height: 1; }
  .capsule-count .unit { font-size: 8px; letter-spacing: .5px; margin-top: 3px; }
  .key-facts {
    position: absolute; left: 178px; top: 668px; list-style: none;
    font-family: "Open Sans", sans-serif; font-weight: 700;
    font-size: 21px; line-height: 28px; letter-spacing: .5px;
    color: var(--soft-white);
  }
  .fact-rule {
    position: absolute; height: 14px;
    background: repeating-linear-gradient(180deg, var(--label-red) 0 3px, transparent 3px 6px);
  }
  .fact-rule.upper { left: 500px; right: 40px; top: 720px; }
  .fact-rule.lower-left { left: 40px; width: 112px; top: 782px; }
  .fact-rule.lower-right { right: 40px; width: 112px; top: 782px; }
  .supplement-note {
    position: absolute; left: 0; right: 0; top: 768px; text-align: center;
    font-family: "Open Sans", sans-serif; font-weight: 800;
    font-size: 30px; letter-spacing: 1px; color: var(--soft-white);
  }
</style>
</head>
<body>
  <main class="canvas">
    <section class="label">
      <div class="title-band">
        <span class="stripes left"></span>
        <h1 class="product-name">TESTOSTERONE</h1>
        <span class="stripes right"></span>
      </div>
      <h2 class="product-sub">BOOSTER FOR MEN</h2>

      <div class="hero-art" role="img" aria-label="Illustration of a muscular red bull figure with arms crossed"></div>

      <div class="capsule-count">
        <span class="num">180</span>
        <span class="unit">CAPSULES</span>
      </div>
      <ul class="key-facts">
        <li>STAMINA</li>
        <li>MAXIMUM POWER</li>
        <li>EXTRA STRONG FORMULA</li>
      </ul>
      <span class="fact-rule upper"></span>
      <span class="fact-rule lower-left"></span>
      <p class="supplement-note">DIETARY SUPPLEMENT</p>
      <span class="fact-rule lower-right"></span>
    </section>
  </main>
</body>
</html>
```